Flyer Mail out

Need something urgently designed.

I need a flyer done double sided I have provided CWDG photos and the writing. I do not have any dental surgery stock photos as such but this can be used. We are a mobile dental company that goes out to schools and provide free dental services.

I have attached the written document and would like it double sided A4 paper.

The colours I want is Aqua, Light Blue, dark blue, grey and white.

Just need it designed beautifully and professionally to go out to principals to contact us and use our services.

If you would like more info have a look at our Chatterloop page Coastline Wandering Dental Group

```html
<!DOCTYPE html>
<html lang="en">
<head>
<meta charset="utf-8">
<title>CWDG School Dental Flyer</title>
<link rel="stylesheet" href="https://fonts.googleapis.com/css2?family=Tinos:ital,wght@0,400;0,700;1,400;1,700&family=Oswald:wght@500&display=swap">
<style>
  :root {
    --sky: #b4eef8;
    --sky-deep: #98e3f3;
    --ink: #111111;
    --photo-edge: #ffffff;
    --clinic-tone: #b9c4cc;
    --portrait-tone: #d7d3cf;
    --truck-tone: #a9b7c4;
    --kids-tone: #f4d6bd;
    --kids-shirt: #ef8a6e;
    --staff-tone: #3558b4;
  }
  html, body { margin: 0; padding: 0; overflow: hidden; }
  body { width: 1200px; height: 849px; }
  .flyer {
    position: relative;
    width: 1200px; height: 849px;
    overflow: hidden;
    background: linear-gradient(180deg, var(--sky) 0%, var(--sky-deep) 100%);
    font-family: "Tinos", "Times New Roman", serif;
    color: var(--ink);
  }
  .photo {
    position: absolute;
    border: 5px solid var(--photo-edge);
    box-shadow: 2px 3px 6px rgba(0,0,0,.35);
    box-sizing: border-box;
  }
  .photo--clinic { left: 68px; top: 36px; width: 252px; height: 176px; transform: rotate(6deg); background: linear-gradient(135deg, #8a9aa6, var(--clinic-tone) 60%, #e5ecef); }
  .photo--team { left: 228px; top: 228px; width: 156px; height: 176px; transform: rotate(2deg); background: linear-gradient(160deg, #f1efec, var(--portrait-tone) 55%, #6d6d72); }
  .photo--van { left: 66px; top: 398px; width: 258px; height: 200px; transform: rotate(6deg); background: linear-gradient(180deg, #dfe9f1 0%, var(--truck-tone) 55%, #55606b 100%); }
  .cutout { position: absolute; }
  .cutout--kids { left: 418px; top: 612px; width: 372px; height: 168px; border-radius: 70px 70px 14px 14px; background: linear-gradient(180deg, var(--kids-tone) 0%, #f2c9a8 55%, var(--kids-shirt) 100%); }
  .cutout--staff { left: 818px; top: 596px; width: 382px; height: 253px; border-radius: 120px 130px 0 0; background: linear-gradient(180deg, #4b6cc2 0%, var(--staff-tone) 60%, #24408c 100%); }

  .headline {
    position: absolute; left: 440px; top: 40px; width: 320px;
    margin: 0; text-align: center;
    font-weight: 400; font-size: 27px; line-height: 29px;
  }
  .evidence { position: absolute; left: 480px; top: 160px; width: 330px; font-size: 16.5px; line-height: 20.5px; }
  .evidence p { margin: 0; white-space: nowrap; }
  .evidence .quote { font-style: italic; }
  .evidence .source { margin-bottom: 20px; }
  .call {
    position: absolute; left: 404px; top: 466px; width: 380px; margin: 0;
    text-align: center; font-family: "Oswald", "Arial Narrow", sans-serif;
    font-weight: 500; font-size: 24px; line-height: 34px; letter-spacing: -.3px;
  }
  .call .smile { display: block; font-size: 29px; }
  .contact { position: absolute; left: 832px; top: 124px; width: 360px; font-size: 19.5px; line-height: 23px; }
  .contact p { margin: 0 0 23px; white-space: nowrap; }
  .contact .link { font-weight: 700; }
  .contact .indent { padding-left: 30px; }
  .social { position: absolute; left: 51px; top: 682px; width: 360px; font-size: 16px; line-height: 22px; margin: 0; white-space: nowrap; }
</style>
</head>
<body>
<main class="flyer">
  <div class="photo photo--clinic" role="img" aria-label="Photo of two dental staff treating a patient in the clinic chair"></div>
  <div class="photo photo--team" role="img" aria-label="Photo of two smiling dental assistants in uniform"></div>
  <div class="photo photo--van" role="img" aria-label="Photo of the dental team standing in front of the mobile clinic truck"></div>
  <div class="cutout cutout--kids" role="img" aria-label="Photo of four smiling children resting their chins on their hands"></div>
  <div class="cutout cutout--staff" role="img" aria-label="Photo of three dental staff in blue scrubs"></div>

  <h1 class="headline">“OUR FOCUS IS ON<br>EDUCATION<br>&amp; PREVENTION”</h1>

  <section class="evidence">
    <p class="quote">“1 in 5 children between the ages of<br>4-8 years of age will suffer from tooth<br>decay or dental caries as a result of<br>poor dental hygiene”</p>
    <p class="source">(ref; The Southern Paediatric<br>Health Council)</p>
    <p>Thus, leading to possible dental<br>destruction to their adult teeth.<br>This, in conjunction with diet,<br>lifestyle and social welfare can be<br>contribution to the increase of child<br>absenteeism.</p>
  </section>

  <p class="call">Book us now for 2015 and help us,<br>bring back your student’s<span class="smile">“bright smile”</span></p>

  <section class="contact">
    <p>To find out about our procedures<br>or to book your school for 2015<br>and take advantage of<br>this opportunity,<br>please visit our website:<br><span class="link indent">www.cwdg.net.au</span><br>or email me at:<br><span class="link">Marla.t@cwdg.net.au</span></p>
    <p>Or to speak to one of<br>our friendly staff,<br>call us directly on:<br><span class="link">(02) 5550 1742</span></p>
  </section>

  <p class="social">In addition, feel free to visit Chatterloop<br>page: Coastline Wandering Dental Group /<br>chirpline/linkpost to see regular updates,<br>features, special offers and daily tips<br>regarding our services.</p>
</main>
</body>
</html>
```